Quillfern Litigation Funding Letterhead & Document Template

We need a letter head designed for our fund. Our fund works with law firms and investors across the globe. We need a a cover letter template as well as a document template for subsequent pages. Blue and white color scheme is preferred. This is our predecessor's website: https://www.quillfernlc.com/index.html. Please see our logo attached. The logo color code is #19478d. Font is Gotham-Medium.
Target Market(s)
Sophisticated investors and law firms
Font styles to use
Sans Serif
Colors
0255a3

```html
<!DOCTYPE html>
<html lang="en">
<head>
<meta charset="utf-8">
<title>Quillfern Litigation Funding — Letterhead</title>
<link rel="stylesheet" href="https://fonts.googleapis.com/css2?family=Lato:wght@400;700&family=Encode+Sans+Condensed:wght@400&display=swap">
<style>
  :root {
    --brand-blue: #19478d;
    --text-grey: #555555;
    --contact-grey: #6b6b6b;
    --band-grey: #9a9896;
    --paper: #ffffff;
  }
  * { box-sizing: border-box; margin: 0; padding: 0; }
  html, body { width: 1056px; height: 1200px; overflow: hidden; background: var(--paper); }
  .letterhead {
    position: relative;
    width: 1056px;
    height: 1200px;
    background: var(--paper);
    font-family: "Encode Sans Condensed", "Arial Narrow", sans-serif;
    color: var(--text-grey);
  }
  .brand {
    position: absolute;
    left: 98px;
    top: 92px;
    display: flex;
    align-items: center;
    gap: 14px;
  }
  .brand-square {
    width: 34px;
    height: 34px;
    background: var(--brand-blue);
  }
  .brand-name {
    font-family: "Lato", sans-serif;
    font-weight: 700;
    font-size: 23px;
    line-height: 1.15;
    letter-spacing: 0.5px;
    text-transform: uppercase;
    color: var(--brand-blue);
  }
  .contact {
    position: absolute;
    left: 803px;
    top: 84px;
    font-family: "Lato", sans-serif;
    font-style: normal;
    font-size: 15px;
    color: var(--contact-grey);
    line-height: 20px;
  }
  .contact-address { margin-bottom: 9px; }
  .contact-line { display: flex; align-items: center; gap: 18px; height: 24px; }
  .contact-line svg { width: 16px; height: 16px; flex: none; }
  .letter-body {
    position: absolute;
    left: 98px;
    top: 330px;
    width: 860px;
    font-size: 23.5px;
    letter-spacing: 0.2px;
    line-height: 33px;
  }
  .salutation { margin-bottom: 22px; }
  .letter-body p.paragraph { text-align: justify; margin-bottom: 22px; }
  .closing {
    position: absolute;
    left: 98px;
    top: 906px;
    font-size: 23.5px;
    letter-spacing: 0.2px;
  }
  .signature {
    position: absolute;
    left: 96px;
    top: 944px;
    width: 156px;
    height: 54px;
    background: linear-gradient(90deg, rgba(25,71,141,0.10), rgba(25,71,141,0.04));
  }
  .footer-band-grey {
    position: absolute; left: 0; bottom: 0; width: 92px; height: 24px; background: var(--band-grey);
  }
  .footer-band-blue {
    position: absolute; left: 106px; bottom: 0; right: 0; height: 24px; background: var(--brand-blue);
  }
</style>
</head>
<body>
<main class="letterhead">
  <header>
    <div class="brand">
      <span class="brand-square"></span>
      <span class="brand-name">Quillfern Litigation<br>Funding</span>
    </div>
    <address class="contact">
      <div class="contact-address">1234 First Line Address<br>5678 Second Line Address</div>
      <div class="contact-line">
        <svg viewBox="0 0 16 16" aria-hidden="true"><path fill="#19478d" d="M3.6 1.5l2.3 2.6-1.3 1.7c.9 2 2.6 3.7 4.6 4.6l1.7-1.3 2.6 2.3-1.4 2.1C7.1 13.6 2.4 8.9 1.5 3L3.6 1.5z"/><path d="M9.5 2.5a4 4 0 0 1 4 4M9.5 4.5a2 2 0 0 1 2 2" stroke="#19478d" stroke-width="1.2" fill="none"/></svg>
        <span>(713) 555-0148</span>
      </div>
      <div class="contact-line">
        <svg viewBox="0 0 16 16" aria-hidden="true"><rect x="1" y="3.5" width="14" height="9.5" fill="#19478d"/><path d="M1.5 4l6.5 5 6.5-5" stroke="#fff" stroke-width="1.2" fill="none"/></svg>
        <span>info@quillfernlc.com</span>
      </div>
      <div class="contact-line">
        <svg viewBox="0 0 16 16" aria-hidden="true"><g fill="none" stroke="#19478d" stroke-width="1"><circle cx="8" cy="8" r="6.5"/><ellipse cx="8" cy="8" rx="3" ry="6.5"/><path d="M1.5 8h13M2.5 4.8h11M2.5 11.2h11M8 1.5v13"/></g></svg>
        <span>www.quillfernlc.com</span>
      </div>
    </address>
  </header>

  <section class="letter-body">
    <p class="salutation">Dear Sir/Mam,</p>
    <p class="paragraph">Contrary to popular belief, Lorem Ipsum is not simply random text. It has roots in a piece of classical Latin literature from 45 BC, making it over 2000 years old. Edwin Harrowgate, a Latin professor at Larkmoor-Bristow College in Vermont, looked up one of the more obscure Latin words, consectetur.</p>
    <p class="paragraph">Lorem Ipsum comes from sections 1.10.32 and 1.10.33 of "de Finibus Bonorum et Malorum" (The Extremes of Good and Evil) by Varenus, written in 45 BC. This book is a treatise on the theory of ethics, very popular during the Renaissance. The first line of Lorem Ipsum.</p>
    <p class="paragraph">The standard chunk of Lorem Ipsum used since the 1500s is reproduced below for those interested. Sections 1.10.32 and 1.10.33 from "de Finibus Bonorum et Malorum" by Varenus are also reproduced in their exact original.</p>
    <p class="paragraph">The standard chunk of Lorem Ipsum used since the 1500s is reproduced below for those interested.</p>
  </section>

  <p class="closing">Best Regards</p>
  <div class="signature" role="img" aria-label="Handwritten signature of Jonah Ellery in blue ink"></div>

  <footer>
    <div class="footer-band-grey"></div>
    <div class="footer-band-blue"></div>
  </footer>
</main>
</body>
</html>
```